Business Card Design for Photographer

Updating business card design. Must use included logo. We're a luxury wedding photography business. Elegancy, luxury, consistency are messages we wish to convey.

Visit our website at www.colbyvarnway.com to familiarize yourself more with our brand design currently (fonts, colors etc.). This is what we want to maintain.

Target Market(s)

Luxury Brides and Grooms

Industry/Entity Type

Wedding

Contact Information for Business Card

Current logo (attached to brief)
Name: Colby Varnway
Phone: 5208813047
website/blog
Email

Requirements
Must have
• Current logo (attached to brief)
• Name: Colby Varnway
• Phone: 5208813047
• website/blog
• Email
• Instagram username
Should not have
• bright colors, fonts that don't suit our brand (visit www.colbyvarnway.com)

```html
<!DOCTYPE html>
<html lang="en">
<head>
<meta charset="utf-8">
<title>Colby Varnway Photographers — Business Card</title>
<link rel="stylesheet" href="https://fonts.googleapis.com/css2?family=EB+Garamond:ital,wght@0,400;1,400;1,600&family=Marcellus&display=swap">
<style>
  :root {
    --backdrop: #2b2b2b;
    --card-grey: #6b6b6b;
    --card-white: #f4f4f4;
    --ink: #5e5e5e;
    --ink-soft: #7a7a7a;
    --rule: #c4c4c4;
    --on-grey: #ffffff;
  }
  * { box-sizing: border-box; margin: 0; padding: 0; }
  html, body {
    width: 1200px; height: 900px; overflow: hidden;
    background: var(--backdrop);
  }
  .canvas {
    width: 1200px; height: 900px;
    display: flex; flex-direction: column;
    align-items: center; justify-content: center; gap: 50px;
  }
  .card {
    width: 630px; height: 360px; position: relative;
    box-shadow: 0 6px 18px rgba(0,0,0,.35);
  }
  /* Back of card */
  .card-back {
    background: linear-gradient(160deg, #777 0%, var(--card-grey) 55%, #5f5f5f 100%);
    display: flex; flex-direction: column; align-items: center; justify-content: center;
    color: var(--on-grey);
  }
  .brand-mark {
    width: 62px; height: 52px; background: var(--on-grey); margin-bottom: 18px;
  }
  .brand-name {
    font-family: "Marcellus", serif; font-size: 38px; letter-spacing: .32em;
    text-transform: uppercase; margin-right: -.32em; line-height: 1;
  }
  .brand-tagline {
    font-family: "Marcellus", serif; font-size: 17px; letter-spacing: .38em;
    text-transform: uppercase; margin-top: 12px; margin-right: -.38em;
  }
  /* Front of card */
  .card-front {
    background: var(--card-white);
    display: flex; align-items: center;
    padding: 0 48px 0 70px;
  }
  .logo-block {
    display: flex; flex-direction: column; align-items: center; gap: 10px;
    width: 170px;
  }
  .logo-square { width: 140px; height: 118px; background: var(--ink); }
  .logo-name {
    font-family: "Marcellus", serif; font-size: 14px; letter-spacing: .18em;
    text-transform: uppercase; color: var(--ink);
  }
  .contact-block { margin-left: auto; width: 250px; margin-top: -30px; }
  .holder-name {
    font-family: "EB Garamond", serif; font-style: italic; font-size: 26px;
    color: var(--ink); margin-bottom: 26px; padding-left: 0;
  }
  .holder-name .given { font-weight: 600; }
  .contact-list {
    list-style: none; border-left: 1px solid var(--rule);
    padding: 2px 0 4px 12px;
  }
  .contact-item {
    display: flex; align-items: center; gap: 10px;
    font-family: "EB Garamond", serif; font-style: italic; font-size: 15px;
    color: var(--ink-soft); line-height: 1.75;
  }
  .contact-item.phone { font-style: normal; }
  .contact-icon { width: 12px; height: 12px; flex: none; }
  .handle-square { width: 10px; height: 10px; background: var(--ink-soft); flex: none; margin: 0 1px; }
</style>
</head>
<body>
<main class="canvas">
  <section class="card card-back">
    <div class="brand-mark"></div>
    <p class="brand-name">Colby Varnway</p>
    <p class="brand-tagline">Photographers</p>
  </section>

  <section class="card card-front">
    <div class="logo-block">
      <div class="logo-square"></div>
      <p class="logo-name">Colby Varnway</p>
    </div>
    <div class="contact-block">
      <p class="holder-name"><span class="given">Colby</span> Varnway</p>
      <ul class="contact-list">
        <li class="contact-item phone">
          <svg class="contact-icon" viewBox="0 0 24 24"><path fill="#7a7a7a" d="M6.6 10.8a15.1 15.1 0 0 0 6.6 6.6l2.2-2.2c.3-.3.7-.4 1-.2 1.1.4 2.3.6 3.6.6.6 0 1 .4 1 1V20c0 .6-.4 1-1 1A17 17 0 0 1 3 4c0-.6.4-1 1-1h3.5c.6 0 1 .4 1 1 0 1.3.2 2.5.6 3.6.1.3 0 .7-.2 1z"/></svg>
          (520) 881-3047
        </li>
        <li class="contact-item">
          <svg class="contact-icon" viewBox="0 0 24 24"><rect x="2" y="5" width="20" height="14" fill="#7a7a7a"/><path d="M2 5l10 8 10-8" fill="none" stroke="#f4f4f4" stroke-width="2"/></svg>
          colby@colbyvarnway.com
        </li>
        <li class="contact-item">
          <svg class="contact-icon" viewBox="0 0 24 24"><g fill="none" stroke="#7a7a7a" stroke-width="2"><circle cx="12" cy="12" r="10"/><ellipse cx="12" cy="12" rx="4" ry="10"/><path d="M2 12h20"/></g></svg>
          www.colbyvarnway.com
        </li>
        <li class="contact-item">
          <span class="handle-square"></span>
          colbyvarnwayphoto
        </li>
      </ul>
    </div>
  </section>
</main>
</body>
</html>
```